Satchel & Compass needs new business card design

I need a new business card design. I'm looking for out-of-the-box design which represents the freedom of being a location independent entrepreneur.
I offer coaching, retreats and trips.
I would like to see designs with and without the photo.
Colors I use are black (#000000), green (#25A796) and brown (#D7C38C)
Website satchelandcompass.com

Target Market(s)

location independent entrepreneurs, digital nomads, people looking to swap the 9 to 5 for a lifestyle business

Industry/Entity Type

Business

Contact Information for Business Card

Petra Varga
Your Lifestyle Business Coach, Retreat & Trip Leader
http://satchelandcompass.com
hello@satchelandcompass.com
Live a life you don't need a holiday from

Font styles to use
Serif
Sans Serif

Requirements
Must have
• One side should contain only the logo. I would also consider having the "Live a life you don't need a holiday from" on that side too (depending on how it looks)
• Please show both sides on the designs.

```html
<!DOCTYPE html>
<html lang="en">
<head>
<meta charset="utf-8">
<title>Satchel &amp; Compass — Business Card</title>
<link href="https://fonts.googleapis.com/css2?family=Open+Sans:wght@400;600&family=Great+Vibes&display=swap" rel="stylesheet">
<style>
  :root {
    --page: #ececec;
    --card: #231f20;
    --gold: #d7c38c;
    --gold-deep: #b8975a;
    --gold-light: #f1e2b8;
    --ink: #231f20;
    --white: #ffffff;
    --teal: #25a796;
  }
  * { box-sizing: border-box; margin: 0; padding: 0; }
  html, body { width: 1200px; height: 1200px; overflow: hidden; background: var(--page); }
  body { position: relative; font-family: "Open Sans", Arial, sans-serif; }

  .card {
    position: absolute;
    left: 238px;
    width: 724px;
    height: 466px;
    background: var(--card);
    box-shadow: 0 6px 14px rgba(0,0,0,0.25);
    overflow: hidden;
  }
  .card--front { top: 82px; }
  .card--back { top: 617px; }

  .frame { position: absolute; inset: 0; width: 724px; height: 466px; }

  .ring-ornament {
    position: absolute;
    left: 0; top: 0;
    width: 215px; height: 330px;
    border-bottom-right-radius: 50% 45%;
    background: radial-gradient(circle at 35% 35%, rgba(215,195,140,0.55), rgba(184,151,90,0.35) 55%, rgba(35,31,32,0) 100%);
  }
  .card--back .ring-ornament { height: 270px; }

  .brand-name {
    position: absolute;
    left: 0; right: 0;
    top: 200px;
    text-align: center;
    font-family: "Open Sans", Arial, sans-serif;
    font-weight: 600;
    font-size: 40px;
    letter-spacing: 1px;
    color: var(--gold);
    padding-left: 150px;
  }
  .divider {
    position: absolute;
    left: 46px; top: 333px;
    width: 636px; height: 2px;
    background: linear-gradient(90deg, rgba(255,255,255,0.3), var(--white) 20%, var(--white) 80%, rgba(255,255,255,0.3));
  }
  .tagline {
    position: absolute;
    left: 0; right: 0;
    top: 358px;
    text-align: center;
    font-family: "Great Vibes", cursive;
    font-size: 34px;
    color: var(--white);
  }

  .name-band {
    position: absolute;
    left: 200px; top: 135px;
    width: 496px; height: 40px;
    background: linear-gradient(180deg, var(--gold-light), var(--gold) 55%, var(--gold-deep));
  }
  .person-name {
    position: absolute;
    left: 226px; top: 136px;
    font-size: 27px;
    font-weight: 400;
    color: var(--ink);
    line-height: 38px;
  }
  .role {
    position: absolute;
    left: 186px; top: 192px;
    font-size: 19.5px;
    color: var(--white);
  }
  .contact-list { position: absolute; left: 307px; top: 308px; list-style: none; }
  .contact-item {
    display: flex; align-items: center;
    height: 32px; margin-bottom: 9px;
    font-size: 22px; color: var(--white);
  }
  .contact-icon {
    width: 28px; height: 28px; border-radius: 50%;
    background: var(--gold);
    display: flex; align-items: center; justify-content: center;
    margin-right: 21px;
    color: var(--ink); font-size: 12px; font-weight: 600;
  }
</style>
</head>
<body>

<section class="card card--front">
  <svg class="frame" viewBox="0 0 724 466" aria-hidden="true">
    <defs>
      <linearGradient id="goldLine" x1="0" y1="0" x2="1" y2="1">
        <stop offset="0" stop-color="#b8975a"/>
        <stop offset="0.5" stop-color="#f1e2b8"/>
        <stop offset="1" stop-color="#c9a866"/>
      </linearGradient>
    </defs>
    <path d="M200 27 H697 V356 Q697 437 616 437 H29 V294" fill="none" stroke="url(#goldLine)" stroke-width="4"/>
  </svg>
  <div class="ring-ornament" role="img" aria-label="Gold concentric ring ornament in the corner"></div>
  <p class="brand-name">Satchel &amp; Compass</p>
  <div class="divider"></div>
  <p class="tagline">Live a life you don't need a holiday from</p>
</section>

<section class="card card--back">
  <svg class="frame" viewBox="0 0 724 466" aria-hidden="true">
    <path d="M200 27 H697 V358 Q697 439 616 439 H29 V265" fill="none" stroke="url(#goldLine)" stroke-width="4"/>
  </svg>
  <div class="name-band"></div>
  <div class="ring-ornament" role="img" aria-label="Gold concentric ring ornament in the corner"></div>
  <p class="person-name">Petra Varga</p>
  <p class="role">Your Lifestyle Business Coach, Retreat &amp; Trip Leader</p>
  <ul class="contact-list">
    <li class="contact-item">
      <span class="contact-icon">
        <svg width="12" height="12" viewBox="0 0 12 12" aria-hidden="true"><path d="M6 1 L11 6 H9.5 V11 H7 V8 H5 V11 H2.5 V6 H1 Z" fill="#231f20"/></svg>
      </span>
      http://satchelandcompass.com
    </li>
    <li class="contact-item">
      <span class="contact-icon">@</span>
      hello@satchelandcompass.com
    </li>
  </ul>
</section>

</body>
</html>
```